Bodywork Quietude Business Card Design

I want to create a very elegant and sophisticated two sided business card for my massage practice (www.bodyworkquietude.net). I have attached the logo and a PDF with some ideas down for the back of the card but I am open to suggestions. I will want to tie in a post card and flyer to the card later.
Similar colors to website would be great.
Target Market(s)
High end clientele, people looking for a sophisticated spa experience.
Industry/Entity Type
Massage
Contact Information for Business Card
Bodywork Quietude
7318 Larkspur Ave S, Suite 305
Seattle, WA 98103
(206) 555-0147
www.bodyworkquietude.net
Look and feel

```html
<!DOCTYPE html>
<html lang="en">
<head>
<meta charset="utf-8">
<title>Bodywork Quietude – Business Card</title>
<link rel="stylesheet" href="https://fonts.googleapis.com/css2?family=Source+Sans+3:wght@400&family=Marcellus+SC&display=swap">
<style>
  :root {
    --backdrop: #e3e3e3;
    --teal-deep: #123447;
    --cream-edge: #ece6d4;
    --cream-text: #e4dcc6;
    --stone: #d9d3c5;
    --navy-ink: #1c3346;
    --logo-grey: #85878a;
    --service-grey: #7c7f80;
    --rule: #b9b3a6;
  }
  * { box-sizing: border-box; margin: 0; padding: 0; }
  html, body {
    width: 1200px;
    height: 1200px;
    overflow: hidden;
    background: var(--backdrop);
  }
  .sheet {
    width: 1200px;
    height: 1200px;
    display: flex;
    flex-direction: column;
    align-items: center;
    justify-content: center;
    gap: 60px;
  }
  .card {
    width: 900px;
    height: 514px;
    position: relative;
    box-shadow: 0 6px 18px rgba(0,0,0,0.12);
  }

  /* Front side */
  .card-front {
    background: var(--cream-edge);
    padding: 16px;
  }
  .front-panel {
    width: 100%;
    height: 100%;
    background: var(--teal-deep);
    display: flex;
    flex-direction: column;
    align-items: center;
    justify-content: center;
    gap: 70px;
  }
  .front-logo {
    display: flex;
    align-items: center;
    gap: 18px;
    color: var(--cream-text);
    font-family: "Source Sans 3", sans-serif;
    font-weight: 400;
    font-size: 44px;
    letter-spacing: 1px;
  }
  .logo-dot {
    width: 18px;
    height: 18px;
    border-radius: 50%;
    background: currentColor;
  }
  .front-qualities {
    font-family: "Marcellus SC", serif;
    font-size: 21px;
    letter-spacing: 2px;
    color: var(--cream-text);
    display: flex;
    gap: 16px;
  }
  .front-qualities .sep { opacity: 0.8; }

  /* Back side */
  .card-back {
    background: linear-gradient(170deg, #ddd7ca 0%, var(--stone) 60%, #d3cdbf 100%);
    display: flex;
    flex-direction: column;
    align-items: center;
  }
  .back-logo {
    margin-top: 82px;
    display: flex;
    align-items: center;
    gap: 12px;
    color: var(--logo-grey);
    font-family: "Source Sans 3", sans-serif;
    font-weight: 400;
    font-size: 24px;
    letter-spacing: 1px;
  }
  .back-logo .logo-dot { width: 11px; height: 11px; }
  .business-name {
    margin-top: 78px;
    font-family: "Source Sans 3", sans-serif;
    font-weight: 400;
    font-size: 33px;
    color: var(--navy-ink);
  }
  .contact {
    margin-top: 16px;
    font-family: "Source Sans 3", sans-serif;
    font-size: 23px;
    line-height: 31px;
    color: var(--navy-ink);
    text-align: center;
    font-style: normal;
  }
  .services {
    position: absolute;
    left: 0;
    right: 0;
    bottom: 32px;
    border-top: 1px solid var(--rule);
    padding-top: 12px;
    display: flex;
    justify-content: center;
    gap: 10px;
    font-family: "Marcellus SC", serif;
    font-size: 15px;
    letter-spacing: 1.2px;
    color: var(--service-grey);
  }
</style>
</head>
<body>
<main class="sheet">
  <section class="card card-front" aria-label="Business card front">
    <div class="front-panel">
      <div class="front-logo"><span class="logo-dot"></span>Bodywork Quietude</div>
      <p class="front-qualities">
        <span>Unique</span><span class="sep">|</span>
        <span>Invitingly Deep</span><span class="sep">|</span>
        <span>Relaxing</span>
      </p>
    </div>
  </section>

  <section class="card card-back" aria-label="Business card back">
    <div class="back-logo"><span class="logo-dot"></span>Bodywork Quietude</div>
    <h1 class="business-name">Bodywork Quietude</h1>
    <address class="contact">
      7318 Larkspur Ave S, Suite 305<br>
      Seattle, WA 98103<br>
      (206) 555-0147<br>
      www.bodyworkquietude.net
    </address>
    <p class="services">
      <span>Deep Lomi</span><span>|</span>
      <span>Ultra Relaxation</span><span>|</span>
      <span>Nurturing Touch</span><span>|</span>
      <span>Cupping</span><span>|</span>
      <span>Thai Yoga Massage</span><span>|</span>
      <span>Couple’s Massage</span>
    </p>
  </section>
</main>
</body>
</html>
```